Corwin Crest Homes Needs Business Card Design

Looking for a unique modern business card to fit my new Logo.
Name: Marcus Corwin
Company: Corwin Crest Homes, LLC
Tag Line: Always Crafted Right
Email: corwincresthomes@mailnest.example
Phone: (555) 017-2846
Website: www.corwincresthomes.example
License: CORWICH462KX

```html
<!DOCTYPE html>
<html lang="en">
<head>
<meta charset="utf-8">
<title>Corwin Crest Homes — Business Card</title>
<link rel="stylesheet" href="https://fonts.googleapis.com/css2?family=Montserrat:wght@400;500;700;800&display=swap">
<style>
  :root {
    --blue: #1a9ad6;
    --ink: #141414;
    --card-dark: #161616;
    --paper: #ffffff;
    --stage: #e9ebee;
    --light-text: #f2f2f2;
  }
  * { box-sizing: border-box; margin: 0; padding: 0; }
  html, body { width: 1200px; height: 1200px; overflow: hidden; }
  body {
    background: var(--stage);
    font-family: "Montserrat", sans-serif;
    position: relative;
  }
  .card {
    position: absolute;
    left: 150px;
    width: 900px;
    height: 514px;
    border-radius: 40px;
    overflow: hidden;
    border-bottom: 6px solid var(--blue);
    box-shadow: 0 14px 30px rgba(0,0,0,.18);
  }
  .card--front { top: 50px; background: var(--card-dark); }
  .card--back { top: 630px; background: var(--card-dark); }

  /* front: white upper field */
  .front-top {
    position: absolute; left: 0; top: 0; width: 100%; height: 262px;
    background: var(--paper);
  }
  .front-rule {
    position: absolute; left: 0; top: 262px; width: 100%; height: 8px;
    background: var(--blue);
    border-bottom: 10px solid var(--paper);
    box-sizing: content-box;
  }
  .brand {
    position: absolute; top: 84px; left: 0; width: 100%;
    display: flex; align-items: center; justify-content: center; gap: 22px;
  }
  .brand-mark {
    width: 58px; height: 58px; background: var(--blue);
  }
  .brand-name {
    font-weight: 800; font-size: 46px; letter-spacing: 1px;
    color: var(--ink); text-transform: uppercase;
  }
  .tagline {
    position: absolute; top: 192px; left: 0; width: 100%;
    text-align: center; font-weight: 500; font-size: 19px;
    letter-spacing: 6px; color: var(--ink); text-transform: uppercase;
  }

  /* front: dark lower field */
  .owner {
    position: absolute; left: 60px; top: 345px;
  }
  .owner-name {
    font-weight: 700; font-size: 38px; color: var(--blue);
    text-transform: uppercase; letter-spacing: -.5px; line-height: 1.1;
  }
  .owner-line {
    font-weight: 400; font-size: 18px; color: var(--light-text);
    text-transform: uppercase; line-height: 1.35;
  }
  .divider {
    position: absolute; left: 440px; top: 318px; width: 1px; height: 150px;
    background: #4a4a4a;
  }
  .contacts {
    position: absolute; left: 470px; top: 332px;
    list-style: none;
  }
  .contacts li {
    display: flex; align-items: center; gap: 12px;
    font-size: 18px; color: var(--light-text); height: 40px;
    white-space: nowrap;
  }
  .contacts svg { width: 22px; height: 22px; flex: none; }

  /* back */
  .back-brand {
    position: absolute; top: 50%; left: 0; width: 100%;
    transform: translateY(-50%);
    display: flex; align-items: center; justify-content: center; gap: 26px;
  }
  .back-brand .brand-name { color: var(--paper); font-size: 54px; }
  .back-brand .brand-mark { width: 68px; height: 68px; }
</style>
</head>
<body>
  <section class="card card--front">
    <div class="front-top">
      <div class="brand">
        <span class="brand-mark"></span>
        <span class="brand-name">Corwin Crest Homes</span>
      </div>
      <p class="tagline">Always Crafted Right</p>
    </div>
    <div class="front-rule"></div>

    <div class="owner">
      <p class="owner-name">Marcus Corwin</p>
      <p class="owner-line">Corwin Crest Homes, LLC</p>
      <p class="owner-line">License: CORWICH462KX</p>
    </div>

    <div class="divider"></div>

    <ul class="contacts">
      <li>
        <svg viewBox="0 0 24 24" fill="var(--blue)" aria-hidden="true"><path d="M6.6 10.8a15.1 15.1 0 0 0 6.6 6.6l2.2-2.2a1 1 0 0 1 1-.25 11.4 11.4 0 0 0 3.6.57 1 1 0 0 1 1 1V20a1 1 0 0 1-1 1A17 17 0 0 1 3 4a1 1 0 0 1 1-1h3.5a1 1 0 0 1 1 1c0 1.25.2 2.46.57 3.6a1 1 0 0 1-.25 1z"/></svg>
        (555) 017-2846
      </li>
      <li>
        <svg viewBox="0 0 24 24" aria-hidden="true"><rect x="2" y="5" width="20" height="14" fill="var(--blue)"/><path d="M2 5l10 8 10-8M2 19l8-7M22 19l-8-7" stroke="var(--card-dark)" stroke-width="1.6" fill="none"/></svg>
        corwincresthomes@mailnest.example
      </li>
      <li>
        <svg viewBox="0 0 24 24" fill="none" stroke="var(--blue)" stroke-width="1.8" aria-hidden="true"><circle cx="12" cy="12" r="9.5"/><ellipse cx="12" cy="12" rx="4" ry="9.5"/><path d="M2.5 12h19M4 7h16M4 17h16"/></svg>
        www.corwincresthomes.example
      </li>
    </ul>
  </section>

  <section class="card card--back">
    <div class="back-brand">
      <span class="brand-mark"></span>
      <span class="brand-name">Corwin Crest Homes</span>
    </div>
  </section>
</body>
</html>
```